Software Specialist in Artificial Intelligence innovation needs a smart and professional looking bus

Prefers a clean and professional design, yet portraying a class of its own and a world-class feel. We develop state-of-the-art software automation engines by deploying artificial intelligence that simulates the smartest brains that are able to simulate a human consultant and/or data scientist. Both single-sided or double-sided design is acceptable. Do not refer too much to our current website as we are also in the process of revamping it so that it better reflects who we are and what we do.
Updates

Project Deadline Extended
Reason: A substantial number of designs submitted to date deviates a fair bit from requirements and expectations. Feedbacks will be provided to all parties by today and as such, an extension is catered to accomodate re-submissions.

Target Market(s)

Software technology companies, software developers, enterprise clients that requires automation supported by Artificial Intelligence driven software solutions.

Industry/Entity Type

Software

Contact Information for Business Card

Marcus Tan
Chief Innovator
marcustan@veltrixia.com
mobile: +65 94567312
Company Name: Veltrixia Pte Ltd
Address: 14 Sorbank Road #05-11 Harlowe Point, Singapore 538422
Telephone: +65 63417250
Website: www.Veltrixia.com
Please do not include the titles of the above fields.

Font styles to use
Sans Serif
Other font styles liked:
• Calibri, Futura Condensed

Requirements
Must have
• Portrays a professional and innovative image. Should reflect that the company is into Artificial Intelligence software development, high tech kind of feel.
Nice to have
• A plus point would be if you can even come up with a new company logo for us, representing who we are. Our current company logo is attached.
Should not have
• Fanciful stuffs as it must portray a professional image. Prefers not to have the cloud "image" as part of the logo or in the name card.

```html
<!DOCTYPE html>
<html lang="en">
<head>
<meta charset="utf-8">
<title>Veltrixia Pte Ltd — Marcus Tan</title>
<link href="https://fonts.googleapis.com/css2?family=ABeeZee&display=swap" rel="stylesheet">
<style>
  :root {
    --card-deep: #0d0d0d;
    --card-mid: #262626;
    --card-soft: #3a3a3a;
    --text-bright: #ffffff;
    --text-muted: #a8a6a4;
  }
  html, body {
    margin: 0;
    padding: 0;
    width: 1200px;
    height: 722px;
    overflow: hidden;
    background: var(--card-deep);
  }
  .business-card {
    position: relative;
    width: 1200px;
    height: 722px;
    overflow: hidden;
    font-family: "ABeeZee", sans-serif;
  }
  .card-backdrop {
    position: absolute;
    inset: 0;
    width: 100%;
    height: 100%;
  }
  .company-name {
    position: absolute;
    left: 151px;
    top: 129px;
    margin: 0;
    font-size: 44px;
    line-height: 52px;
    font-weight: 400;
    color: var(--text-bright);
    white-space: nowrap;
  }
  .company-details {
    position: absolute;
    left: 155px;
    margin: 0;
    font-size: 30px;
    line-height: 40.5px;
    color: var(--text-muted);
    font-style: normal;
    white-space: nowrap;
  }
  .company-address { top: 193px; }
  .company-contact { top: 357px; }
  .person-name {
    position: absolute;
    left: 644px;
    top: 438px;
    margin: 0;
    font-size: 72px;
    line-height: 80px;
    font-weight: 400;
    color: var(--text-bright);
    white-space: nowrap;
  }
  .person-details {
    position: absolute;
    left: 706px;
    top: 515px;
    margin: 0;
    font-size: 23.5px;
    line-height: 30px;
    color: var(--text-muted);
    font-style: normal;
    white-space: nowrap;
  }
</style>
</head>
<body>
  <main class="business-card">
    <svg class="card-backdrop" role="img" aria-label="Dark faceted geometric crystal pattern in black and charcoal tones" viewBox="0 0 1200 722" preserveAspectRatio="none">
      <defs>
        <radialGradient id="backdrop-glow" cx="0.62" cy="0.42" r="0.8">
          <stop offset="0" stop-color="var(--card-soft)"/>
          <stop offset="0.55" stop-color="var(--card-mid)"/>
          <stop offset="1" stop-color="var(--card-deep)"/>
        </radialGradient>
      </defs>
      <rect width="1200" height="722" fill="url(#backdrop-glow)"/>
    </svg>

    <h1 class="company-name">Veltrixia Pte Ltd</h1>
    <address class="company-details company-address">
      14 Sorbank Road,<br>
      #05-11 Harlowe Point,<br>
      Singapore, 538422
    </address>
    <p class="company-details company-contact">
      www.Veltrixia.com<br>
      T: +65 63417250
    </p>

    <h2 class="person-name">Marcus Tan</h2>
    <address class="person-details">
      Chief Inovator<br>
      marcustan@veltrixia.com<br>
      M: +65 94567312
    </address>
  </main>
</body>
</html>
```